Box and Paper Bag Design
for exclusive line of prescriptions creams
Box and Paper Bag Design  - Health
Creative Brief
A design for the box (layout attached) and a promotional paper bag (no layout - see sample picture: 8" length, 7" high, 3.5" deep) - front and back designs will be fine. Both packages are for exclusive line of prescription creams. Should resemble expensive, high end, sophisticated and upscale style, yet THIS IS PRESCRIPTION MEDICATION - the packaging should resemble this also. FRONT: 1. Logo (attached) 2. Text: Professional Prescription Formula Dispensed Only By Physicians 3. On the bottom: e 30 ml / 1 fl.oz. Made in USA BACK: All the way on the bottom - try to fit into lower 1/4th of the space: Directions: Follow the directions of your prescribing Physician Cautions: For external use only - do not ingest. Avoid contact with open wounds. Avoid getting into eyes. Make sure skin is clean and dry before applying . Discontinue use if rash or discomfort occurs. Not for use by pregnant or lactating women. The packaging is NOT child resistant. KEEP AWAY FROM CHILDREN. If accidentally ingested seek medical help immediately. _________________________ We will be using various technics while printing the boxes: uv coating, spot foil etc See several samples of the designs I liked attached. Try to stick to conservative yet fresh colors: metallic, silver, gray , blue, green.
Health
Doctors, medical professionals and their patients.

```html
<!DOCTYPE html>
<html lang="en">
<head>
<meta charset="utf-8">
<title>Velmora Rx – Prescription Cream Carton Dieline</title>
<link rel="stylesheet" href="https://fonts.googleapis.com/css2?family=Montserrat:wght@400;500&family=Lato:wght@400;700&display=swap">
<style>
  :root {
    --paper: #ffffff;
    --flap: #c9ccd3;
    --cut: #9ea3ad;
    --ink: #2a3550;
    --ink-soft: #4a5570;
    --tint-lilac: #e7dff0;
    --tint-sky: #d4e3f4;
    --tint-blue: #b9cfec;
    --tint-pearl: #f3f2f8;
  }
  html, body {
    margin: 0;
    padding: 0;
    width: 1200px;
    height: 830px;
    overflow: hidden;
    background: var(--paper);
  }
  .dieline { display: block; width: 1200px; height: 830px; }
  .flap { fill: var(--flap); stroke: var(--cut); stroke-width: 1; }
  .panel { stroke: var(--cut); stroke-width: 1; }
  .brand-name {
    font-family: "Montserrat", sans-serif;
    font-weight: 500;
    font-size: 20px;
    letter-spacing: 3px;
    fill: var(--ink);
  }
  .brand-mark { fill: none; stroke: var(--ink); stroke-width: 2; }
  .claim {
    font-family: "Lato", sans-serif;
    font-weight: 400;
    font-size: 13px;
    fill: var(--ink);
  }
  .volume {
    font-family: "Lato", sans-serif;
    font-size: 11.5px;
    fill: var(--ink);
  }
  .fine-print {
    font-family: "Lato", sans-serif;
    font-size: 5.1px;
    fill: var(--ink-soft);
  }
</style>
</head>
<body>
<svg class="dieline" viewBox="0 0 1200 830" xmlns="http://www.w3.org/2000/svg">
  <defs>
    <linearGradient id="wash" x1="0" y1="0" x2="1" y2="1">
      <stop offset="0" stop-color="var(--tint-lilac)"/>
      <stop offset="0.45" stop-color="var(--tint-pearl)"/>
      <stop offset="0.75" stop-color="var(--tint-sky)"/>
      <stop offset="1" stop-color="var(--tint-blue)"/>
    </linearGradient>
    <linearGradient id="wash-side" x1="0" y1="0" x2="0" y2="1">
      <stop offset="0" stop-color="var(--tint-sky)"/>
      <stop offset="0.35" stop-color="var(--tint-pearl)"/>
      <stop offset="0.6" stop-color="var(--paper)"/>
      <stop offset="1" stop-color="var(--paper)"/>
    </linearGradient>
  </defs>

  <!-- glue flap -->
  <path class="flap" d="M149 204 L96 228 L96 588 L149 612 Z"/>

  <!-- top tuck and lid -->
  <path class="flap" d="M149 67 L149 30 Q149 12 170 12 L356 12 Q377 12 377 30 L377 67 Z"/>
  <rect class="panel" x="149" y="67" width="228" height="137" fill="url(#wash)"
        role="img" aria-label="Soft lilac and blue wave pattern"/>
  <g transform="rotate(180 263 135)">
    <rect class="brand-mark" x="172" y="127" width="13" height="13"/>
    <text class="brand-name" x="194" y="142">VELMORA RX</text>
  </g>

  <!-- dust flaps -->
  <path class="flap" d="M377 204 L392 150 L592 150 L607 204 Z"/>
  <path class="flap" d="M835 204 L850 150 L1053 150 L1068 204 Z"/>
  <path class="flap" d="M377 612 L392 666 L592 666 L607 612 Z"/>
  <path class="flap" d="M835 612 L850 666 L1053 666 L1068 612 Z"/>
  <path class="flap" d="M149 612 L160 650 L366 650 L377 612 Z"/>

  <!-- front panel -->
  <rect class="panel" x="149" y="204" width="228" height="408" fill="url(#wash)"
        role="img" aria-label="Soft lilac and blue wave pattern"/>
  <rect class="brand-mark" x="172" y="341" width="13" height="13"/>
  <text class="brand-name" x="194" y="356">VELMORA RX</text>
  <text class="volume" x="263" y="563" text-anchor="middle">e 30 ml / 1 fl.oz. Made in USA</text>

  <!-- side panel -->
  <rect class="panel" x="377" y="204" width="230" height="408" fill="url(#wash-side)"
        role="img" aria-label="Soft blue wave pattern fading to white"/>
  <text class="claim" x="492" y="278" text-anchor="middle">Professional Prescription Formula</text>
  <text class="claim" x="492" y="295" text-anchor="middle">Dispensed Only By Physicians</text>
  <g class="fine-print">
    <text x="392" y="438">Directions: Follow the directions of your prescribing Physician</text>
    <text x="392" y="451">Cautions: For external use only - do not ingest. Avoid contact with open wounds.</text>
    <text x="392" y="458">Avoid getting into eyes. Make sure skin is clean and dry before applying. Discontinue</text>
    <text x="392" y="465">use if rash or discomfort occurs. Not for use by pregnant or lactating women. The</text>
    <text x="392" y="472">packaging is NOT child resistant. KEEP AWAY FROM CHILDREN. If accidentally ingested</text>
    <text x="392" y="479">seek medical help immediately.</text>
  </g>

  <!-- back panel -->
  <rect class="panel" x="607" y="204" width="228" height="408" fill="url(#wash)"
        role="img" aria-label="Soft lilac and blue wave pattern"/>
  <rect class="brand-mark" x="630" y="341" width="13" height="13"/>
  <text class="brand-name" x="652" y="356">VELMORA RX</text>
  <text class="volume" x="721" y="563" text-anchor="middle">e 30 ml / 1 fl.oz. Made in USA</text>

  <!-- bottom flap -->
  <rect class="panel" x="607" y="612" width="228" height="204" fill="url(#wash)"
        role="img" aria-label="Soft lilac and blue circle pattern"/>

  <!-- second side panel -->
  <rect class="panel" x="835" y="204" width="233" height="408" fill="url(#wash-side)"
        role="img" aria-label="Soft blue wave pattern fading to white"/>
  <text class="claim" x="951" y="278" text-anchor="middle">Professional Prescription Formula</text>
  <text class="claim" x="951" y="295" text-anchor="middle">Dispensed Only By Physicians</text>
  <g class="fine-print">
    <text x="850" y="438">Directions: Follow the directions of your prescribing Physician</text>
    <text x="850" y="451">Cautions: For external use only - do not ingest. Avoid contact with open wounds.</text>
    <text x="850" y="458">Avoid getting into eyes. Make sure skin is clean and dry before applying. Discontinue</text>
    <text x="850" y="465">use if rash or discomfort occurs. Not for use by pregnant or lactating women. The</text>
    <text x="850" y="472">packaging is NOT child resistant. KEEP AWAY FROM CHILDREN. If accidentally ingested</text>
    <text x="850" y="479">seek medical help immediately.</text>
  </g>
</svg>
</body>
</html>
```